The most modern business card ever !!!

Our company call “Vantilo”. Vantilo is a technology company specialized in cruises solutions. Out main product is a platform to reserve cruises. This is a revolutionary platform that make easier to travel agencies and final users to reserve cruises across dozen companies like tarvik, welbi, dpv, hbt, etc..We are a “start up”, with a young team of developers and we want to transmit it.. For it, we want something different, a modern business card that represent cruises and technology.. When someone receive this card, this person should say: wowww this is different… this is modern… this is a cruise related company..
Contact Information for Business Card
Requirements
Must have
- diferent, modern
Should not have
- traditions business card

```html
<!DOCTYPE html>
<html lang="en">
<head>
<meta charset="utf-8">
<title>Vantilo Business Card</title>
<link href="https://fonts.googleapis.com/css2?family=Oswald:wght@500&family=Work+Sans:wght@400;600&display=swap" rel="stylesheet">
<style>
  :root {
    --stage: #1b1b1b;
    --card: #262626;
    --card-edge: #2f2f2f;
    --ink: #ffffff;
    --accent: #1ea6e0;
  }
  html, body {
    margin: 0;
    padding: 0;
    width: 1200px;
    height: 900px;
    overflow: hidden;
    background: var(--stage);
  }
  .canvas {
    position: relative;
    width: 1200px;
    height: 900px;
  }
  .card {
    position: absolute;
    left: 270px;
    width: 660px;
    height: 377px;
    background: linear-gradient(135deg, var(--card) 0%, var(--card-edge) 100%);
    box-shadow: 0 12px 30px rgba(0,0,0,0.45);
    font-family: "Work Sans", sans-serif;
    color: var(--ink);
  }
  .card-front { top: 52px; }
  .card-back { top: 471px; }

  .brand-name {
    position: absolute;
    left: 0;
    right: 0;
    top: 50%;
    transform: translateY(-50%);
    text-align: center;
    font-weight: 600;
    font-size: 84px;
    letter-spacing: 2px;
    color: var(--ink);
  }

  .identity {
    position: absolute;
    right: 390px;
    top: 128px;
    text-align: right;
  }
  .person-name {
    font-family: "Oswald", sans-serif;
    font-weight: 500;
    font-size: 40px;
    line-height: 1;
    letter-spacing: 1px;
    color: var(--accent);
  }
  .person-role {
    margin-top: 8px;
    font-size: 17px;
    letter-spacing: 1.5px;
  }
  .divider {
    position: absolute;
    left: 286px;
    top: 128px;
    width: 2px;
    height: 74px;
    background: var(--accent);
  }
  .contact-list {
    position: absolute;
    left: 306px;
    top: 128px;
    margin: 0;
    padding: 0;
    list-style: none;
    font-size: 17px;
    letter-spacing: 1.5px;
  }
  .contact-list li {
    display: flex;
    align-items: center;
    height: 25px;
  }
  .contact-list svg {
    width: 12px;
    height: 12px;
    margin-right: 10px;
    flex: none;
  }
  .address {
    position: absolute;
    left: 54px;
    bottom: 50px;
    font-size: 18px;
    letter-spacing: 1.5px;
  }
</style>
</head>
<body>
<div class="canvas">
  <section class="card card-front">
    <div class="brand-name">Vantilo</div>
  </section>

  <section class="card card-back">
    <div class="identity">
      <div class="person-name">DARIEN HOLT</div>
      <div class="person-role">Director</div>
    </div>
    <div class="divider"></div>
    <ul class="contact-list">
      <li>
        <svg viewBox="0 0 12 12" aria-hidden="true"><path d="M3 1 L5 3.5 L4 5 Q5.5 7 7 8 L8.5 7 L11 9 L9.5 11 Q4 10 1 2.5 Z" fill="var(--accent)"/></svg>
        (415) 672-9180
      </li>
      <li>
        <svg viewBox="0 0 12 12" aria-hidden="true"><rect x="1" y="2.5" width="10" height="7" fill="none" stroke="var(--accent)" stroke-width="1.2"/><path d="M1 2.5 L6 6.5 L11 2.5" fill="none" stroke="var(--accent)" stroke-width="1.2"/></svg>
        info@vantilo.com.br
      </li>
      <li>
        <svg viewBox="0 0 12 12" aria-hidden="true"><circle cx="6" cy="6" r="5" fill="none" stroke="var(--accent)" stroke-width="1.2"/><ellipse cx="6" cy="6" rx="2.2" ry="5" fill="none" stroke="var(--accent)" stroke-width="1"/><path d="M1 6 H11" stroke="var(--accent)" stroke-width="1"/></svg>
        www.vantilo.com.br
      </li>
    </ul>
    <div class="address">212b Harlow Street, Westbrook, NZ, 4027</div>
  </section>
</div>
</body>
</html>
```